Travinex - You are the Boss!

Travinex is a new Silicon Valley company, of the pelim founders from Berlin, which provides a "Shared Pioneer Circle". This platform allows the crowd to support startups with money, experts and fame. Our Vision is, that everyone should become an entrepreneur.

Pls find all brief details in the attached document
Updates

Would be nice to have a list of more social services I'm available on, like a list of pictograms of all my services:

Find me on: vooka, bramlet+, qrt, fenwix, moodrail, zupp, hvoxa, etc...

pls make sure to use the right font:
http://www.typemarlow.com/fonts/Velquin

Target Market(s)

Main target market is those already involved in the startup industry, by fundraising, investing, advising, cofounding and working. Travinex brings a totaly new transparency and collaborative way of starting companies to that business.

· Entrepreneurs (looking for funding, team and community)
· Investors (looking for hot investments and )
· Experts (workers looking for startups they can work for equity)
· Incubators & Business Schools (looking for tools to advise startups)

Industry/Entity Type

It Company

Requirements
Must have
• Pls find all brief details in the attached document
Nice to have

```html
<!DOCTYPE html>
<html lang="en">
<head>
<meta charset="utf-8">
<title>Travinex business card</title>
<link rel="stylesheet" href="https://fonts.googleapis.com/css2?family=Orbitron:wght@400;500;700&display=swap">
<style>
  :root {
    --orange: #f26b1d;
    --charcoal: #353535;
    --ink: #2b2b2b;
    --paper: #ffffff;
    --backdrop: #ffffff;
    --shadow: rgba(0,0,0,0.35);
  }
  * { box-sizing: border-box; margin: 0; padding: 0; }
  html, body {
    width: 1200px; height: 900px; overflow: hidden;
    background: var(--backdrop);
    font-family: "Orbitron", sans-serif;
  }
  .canvas { position: relative; width: 1200px; height: 900px; }
  .card {
    position: absolute; left: 344px; width: 514px; height: 300px;
    background: var(--paper); overflow: hidden;
    box-shadow: 0 2px 8px var(--shadow);
  }
  .card--front { top: 120px; }
  .card--back { top: 490px; }

  /* front */
  .brand { position: absolute; left: 30px; top: 26px; width: 130px; text-align: center; }
  .brand__dot { display: block; width: 40px; height: 40px; margin: 0 auto 18px; border-radius: 50%; background: var(--orange); }
  .brand__name { font-size: 20px; font-weight: 700; color: var(--ink); letter-spacing: 0.5px; line-height: 24px; }
  .person { position: absolute; right: 22px; top: 72px; text-align: right; color: var(--orange); }
  .person__name { font-size: 20px; font-weight: 500; line-height: 24px; }
  .person__role { font-size: 15px; font-style: italic; line-height: 20px; }
  .rule { position: absolute; left: 0; right: 0; top: 124px; height: 4px; background: var(--orange); }
  .panel { position: absolute; left: 0; right: 0; top: 128px; bottom: 0; background: var(--charcoal); color: #fff; }
  .contact { position: absolute; right: 22px; top: 8px; text-align: right; font-size: 19px; line-height: 22px; }
  .links { position: absolute; right: 22px; top: 62px; text-align: right; font-size: 16px; line-height: 22px; list-style: none; }

  /* back */
  .pitch { position: absolute; left: 36px; top: 52px; color: var(--ink); }
  .pitch__lead { font-size: 19px; font-weight: 500; }
  .pitch__list { list-style: none; margin-top: 16px; margin-left: 8px; font-size: 18px; line-height: 28px; }
  .pitch__list li::before { content: "- "; }
  .invite { position: absolute; left: 0; right: 0; top: 240px; text-align: center; color: var(--orange); font-size: 19px; font-weight: 700; }
</style>
</head>
<body>
<div class="canvas">
  <section class="card card--front">
    <div class="brand">
      <span class="brand__dot"></span>
      <div class="brand__name">Travinex</div>
    </div>
    <div class="person">
      <div class="person__name">Marcus Edler</div>
      <div class="person__role">Founder and CEO</div>
    </div>
    <div class="rule"></div>
    <div class="panel">
      <div class="contact">
        <div>555-555-0199</div>
        <div>me@travinex.com</div>
      </div>
      <ul class="links">
        <li>www.travinex.com</li>
        <li>chirpa.com/marcusedler</li>
        <li>folkbook.com/marcusedler</li>
        <li>linkwork.com/in/marcusedler</li>
      </ul>
    </div>
  </section>

  <section class="card card--back">
    <div class="pitch">
      <div class="pitch__lead">Are you interested in:</div>
      <ul class="pitch__list">
        <li>Starting your own business?</li>
        <li>Investing in hot startups?</li>
        <li>Working for the next “Folkbook”?</li>
      </ul>
    </div>
    <div class="invite">Join us on folkbook.com/Travinex</div>
  </section>
</div>
</body>
</html>
```